Propose a revamped landing page

One template we like eg is https://www.tornavo.com but but cluttered Our logo and colors are attached to our logo and colors are printed on a white background what we have. So font usage ...
Number of Pages Required
1 page

```html
<!DOCTYPE html>
<html lang="de">
<head>
<meta charset="utf-8">
<title>Voltwise – Immer automatisch zum günstigsten Energieanbieter</title>
<link href="https://fonts.googleapis.com/css2?family=Roboto:wght@300;400;500;700&display=swap" rel="stylesheet">
<style>
:root{
  --orange-light:#f8aa1c;
  --orange:#f47a20;
  --orange-deep:#f26322;
  --teal:#12a89d;
  --dark:#3c4548;
  --text:#3a3a3a;
  --muted:#6f7578;
  --white:#ffffff;
  --peach:#fbb98a;
}
*{box-sizing:border-box;margin:0;padding:0}
html,body{width:1200px;height:3093px;overflow:hidden}
body{position:relative;font-family:'Roboto',Arial,sans-serif;color:var(--text);background:var(--white)}
.backdrop{position:absolute;left:0;top:0;width:1200px;height:3093px}
.abs{position:absolute}
.logo{display:flex;align-items:center;gap:8px;font-weight:700;font-size:30px;color:var(--white);letter-spacing:-.5px}
.logo .dot{width:16px;height:16px;border-radius:50%;background:var(--white)}
.nav{left:437px;top:30px;display:flex;gap:30px;align-items:center}
.nav a{color:var(--white);font-size:9.5px;text-decoration:none;text-transform:uppercase;letter-spacing:.3px}
.nav .nav-cta{background:#fb9a48;padding:10px 22px;border-radius:2px}
.hero-title{left:99px;top:160px;width:480px;font-size:27px;line-height:42px;font-weight:500;color:var(--white)}
.hero-text{left:99px;top:256px;width:340px;font-size:10.5px;line-height:19px;color:var(--white)}
.btn-white{background:var(--white);color:var(--orange);font-size:9px;font-weight:700;text-transform:uppercase;display:flex;align-items:center;justify-content:center;border-radius:2px;box-shadow:0 2px 6px rgba(0,0,0,.12)}
.known-title{left:0;width:1200px;top:556px;text-align:center;font-size:23px;color:var(--white);font-weight:400}
.badge{background:rgba(255,255,255,.55);height:12px;border-radius:2px}
.section-title{left:0;width:1200px;text-align:center;font-size:23px;font-weight:400;color:#2b2b2b}
.intro{left:268px;top:874px;width:664px;text-align:center;font-size:11px;line-height:20px;color:var(--muted)}
.price{left:0;width:1200px;top:962px;text-align:center;font-size:13px;font-weight:500;color:#2b2b2b}
.price-note{left:0;width:1200px;top:985px;text-align:center;font-size:8.5px;color:var(--muted)}
.btn-teal{background:var(--teal);color:var(--white);font-size:9px;font-weight:500;text-transform:uppercase;display:flex;align-items:center;justify-content:center;border-radius:2px}
.power-title{left:600px;top:1241px;font-size:22px;color:#2b2b2b}
.power-lead{left:600px;top:1308px;font-size:10.5px;color:#444}
.power-list{left:600px;top:1336px;list-style:none;font-size:10.5px;color:#444}
.power-list li{position:relative;padding-left:20px;height:26px;line-height:18px}
.power-list li::before{content:"";position:absolute;left:2px;top:6px;width:6px;height:6px;border-radius:50%;background:#555}
.power-note{left:600px;top:1448px;width:400px;font-size:7px;line-height:10px;color:#777}
.steps-title{left:247px;top:1770px;font-size:23px;font-weight:500;color:var(--white)}
.step-num{left:355px;top:1842px;width:30px;height:30px;border-radius:50%;background:var(--white);color:var(--orange);font-weight:700;font-size:16px;display:flex;align-items:center;justify-content:center}
.step-name{left:270px;top:1893px;width:200px;text-align:center;font-size:14px;font-weight:500;color:var(--white)}
.step-desc{left:250px;top:1928px;width:240px;text-align:center;font-size:10px;line-height:17px;color:var(--white)}
.dots{left:354px;top:1997px;display:flex;gap:12px}
.dots span{width:7px;height:7px;border-radius:50%;background:var(--white)}
.dots span.off{background:transparent;border:1.5px solid var(--white)}
.phone{left:734px;top:1691px;width:241px;height:495px;border-radius:32px;background:var(--white);border:8px solid #eceef2;box-shadow:0 14px 30px rgba(0,0,0,.18);overflow:hidden}
.phone-notch{position:absolute;left:60px;top:-2px;width:105px;height:16px;background:#eceef2;border-radius:0 0 12px 12px}
.phone-logo{position:absolute;left:22px;top:24px;display:flex;align-items:center;gap:5px;font-weight:700;font-size:17px;color:var(--orange)}
.phone-logo .dot{width:9px;height:9px;border-radius:50%;background:var(--orange)}
.phone-menu{position:absolute;right:18px;top:30px;width:16px;height:10px;border-top:2px solid #333;border-bottom:2px solid #333}
.phone-menu::after{content:"";position:absolute;left:0;top:2px;width:16px;height:2px;background:#333}
.phone-title{position:absolute;left:22px;top:74px;width:190px;font-size:18px;line-height:22px;font-weight:700;color:#222}
.phone-rule{position:absolute;left:22px;top:124px;width:96px;height:3px;background:var(--orange)}
.phone-text{position:absolute;left:22px;top:150px;width:195px;font-size:10.5px;line-height:15px;color:#333}
.phone-ask{position:absolute;left:22px;top:352px;font-size:10.5px;font-weight:700;color:var(--orange)}
.pill{position:absolute;height:24px;border:1.5px solid #333;border-radius:14px;font-size:7.5px;font-weight:700;display:flex;align-items:center;justify-content:center;text-transform:uppercase;color:#333}
.feature{top:2348px;width:260px;text-align:center}
.feature-icon{width:48px;height:48px;margin:0 auto;border-radius:10px;background:linear-gradient(135deg,var(--orange-light),#4a5255)}
.feature h3{margin-top:14px;font-size:14px;font-weight:500;color:#2b2b2b}
.feature p{margin-top:14px;font-size:10.5px;line-height:18px;color:var(--muted)}
.save-title{left:0;width:1200px;top:2688px;text-align:center;font-size:23px;font-weight:500;color:var(--white)}
.field{top:2759px;width:320px;height:37px;background:var(--white);border-radius:2px;font-size:9px;color:#888;padding-left:18px;display:flex;align-items:center}
.foot-head{top:2935px;font-size:12px;font-weight:700;color:var(--white)}
.foot-links{top:2963px;list-style:none;font-size:9px;color:#dfe3e4}
.foot-links li{height:23px}
.socials{left:860px;top:2968px;display:flex;gap:10px}
.socials span{width:24px;height:24px;border-radius:50%;background:var(--white)}
.copyright{left:0;width:1200px;top:3065px;text-align:center;font-size:8px;color:#cfd4d6}
</style>
</head>
<body>
<svg class="backdrop" viewBox="0 0 1200 3093" aria-hidden="true">
  <defs>
    <linearGradient id="warm" x1="0" y1="0" x2="1" y2="0.3">
      <stop offset="0" stop-color="#f8ab1c"/>
      <stop offset="1" stop-color="#f26222"/>
    </linearGradient>
  </defs>
  <path d="M0 0H1200V620Q600 800 0 620Z" fill="url(#warm)"/>
  <rect x="0" y="1639" width="1200" height="499" fill="url(#warm)"/>
  <path d="M0 2660Q600 2560 1200 2660V3093H0Z" fill="#3c4548"/>
  <path d="M1200 1161 C1090 1161 960 1190 890 1250 C830 1300 840 1370 940 1440 C1060 1520 1200 1577 1200 1577Z" fill="none"/>
  <path d="M0 1161 C150 1150 420 1170 490 1260 C540 1330 505 1470 430 1530 C360 1585 220 1580 0 1560Z" fill="#12a89d"/>
</svg>

<div class="abs logo" style="left:99px;top:26px">voltwise<span class="dot"></span></div>
<nav class="abs nav">
  <a>So funktioniert's</a><a>Preise</a><a>Fragen</a><a>Über uns</a><a>Beitrag</a><a>Erfahrungen</a><a>Presseartikel</a>
  <a class="nav-cta">Jetzt anmelden</a>
</nav>

<h1 class="abs hero-title">Immer automatisch zum günstigsten Energieanbieter wechseln</h1>
<p class="abs hero-text">Voltwise spart Ihnen Zeit und Geld, indem Sie ständig automatisch auf die besten Energieangebote umgestellt werden. Treten Sie Zehntausenden von Voltwise-Kunden bei, die im Durchschnitt 415 € pro Jahr sparen.</p>
<div class="abs btn-white" style="left:99px;top:431px;width:113px;height:27px">Jetzt anmelden</div>

<div class="abs" style="left:692px;top:112px;width:470px;height:400px;border-radius:48% 42% 40% 55% / 45% 48% 52% 55%;background:var(--peach)"></div>
<div class="abs" role="img" aria-label="Foto: junger Mann mit Laptop auf einem Sofa vor einer Stadtansicht" style="left:680px;top:104px;width:460px;height:395px;border-radius:48% 42% 40% 55% / 45% 48% 52% 55%;background:linear-gradient(160deg,#c9d3da,#7f8e98 55%,#3b4650)"></div>

<h2 class="abs known-title">Bekannt aus</h2>
<div class="abs badge" style="left:440px;top:612px;width:66px"></div>
<div class="abs badge" style="left:540px;top:612px;width:89px"></div>
<div class="abs badge" style="left:666px;top:612px;width:70px"></div>
<div class="abs badge" style="left:440px;top:645px;width:66px"></div>
<div class="abs badge" style="left:540px;top:645px;width:89px"></div>
<div class="abs badge" style="left:666px;top:645px;width:70px"></div>

<h2 class="abs section-title" style="top:806px">Nie wieder zu viel für Strom &amp; Gas bezahlen</h2>
<p class="abs intro">Vorbei sind die Zeiten von schlechten Deals, mühsamem Tarifvergleich und langweiligen Wechselformularen. Mit dem automatischen Wechselservice für Voltwise wirst du nie wieder zu viel für Strom und Gas bezahlen. Und das, ohne einen Finger zu rühren. Wir kämpfen uns für dich durch den Tarifdschungel. Also spar' dir dein hart verdientes Geld und werde ein Voltwise-Kunde.</p>
<p class="abs price">All dies für nur € 24 / Jahr</p>
<p class="abs price-note">Keine Vorabkosten - kostenlos bis zu Ihrer ersten Einsparung.</p>
<div class="abs btn-teal" style="left:544px;top:1035px;width:112px;height:26px">Jetzt anmelden</div>

<div class="abs" role="img" aria-label="Foto: Familie mit Kleinkind in einer hellen Küche" style="left:0;top:1161px;width:480px;height:400px;border-radius:0 48% 55% 0 / 0 40% 60% 0;background:linear-gradient(135deg,#e9ddd0,#b89a84 55%,#5b4a44)"></div>

<h2 class="abs power-title">Die günstigste aller Superkräfte</h2>
<p class="abs power-lead">Ab <b>24 Euro</b> bist du dabei:</p>
<ul class="abs power-list">
  <li>Service für Strom oder Gas (1 Zähler): 24 Euro /Jahr</li>
  <li>Service für Strom und Gas (2 Zähler): 36 Euro/Jahr</li>
  <li>Die erste Gebühr verrechnen wir dir erst nach deinem ersten Wechsel</li>
  <li>Spare bis zu 850 Euro jährlich Strom- und Gaskosten beim 1. Wechsel*</li>
</ul>
<p class="abs power-note">* Jährliche Ersparnis eines österreichischen Durchschnittshaushalts (3.500 kWh Strom und 15.000 kWh Gasverbrauch) in der Region mit dem größten Einsparpotenzial nach dem ersten Wechsel vom marktgängigen Tarif des lokalen Strom- und Gas-Anbieters zum günstigsten verfügbaren Anbieter laut Vergleichsrechner vom 1.11.2019.</p>

<h2 class="abs steps-title">Wie werde ich Voltwise-Kunde?</h2>
<div class="abs step-num">1</div>
<p class="abs step-name">Einmalig anmelden</p>
<p class="abs step-desc">Jahresrechnung hochladen. Präferenzen auswählen. Anmeldung abschließen.</p>
<div class="abs dots"><span></span><span></span><span class="off"></span></div>

<div class="abs phone">
  <div class="phone-notch"></div>
  <div class="phone-logo">voltwise<span class="dot"></span></div>
  <div class="phone-menu"></div>
  <h3 class="phone-title">Willkommen bei der Anmeldung</h3>
  <div class="phone-rule"></div>
  <p class="phone-text">Du bist nur wenige Klicks davon entfernt, Voltwise-Kunde zu werden. Das bedeutet, nie wieder zu viel für Strom &amp; Gas zu bezahlen! Denn mit unserem automatischen Energieanbieter-Wechselservice wechselst du jedes Jahr deinen Energieanbieter und sparst dir durch attraktive Rabatte eine ganze Menge Geld - ohne einen Finger zu rühren!</p>
  <p class="phone-ask">Hast du deine Jahresrechnung dabei?</p>
  <div class="pill" style="left:58px;top:390px;width:110px">Ja, weiter anmelden</div>
  <div class="pill" style="left:22px;top:422px;width:180px">Nein, ich muss sie erst suchen</div>
</div>

<h2 class="abs section-title" style="top:2264px">Einmal anmelden, immer sparen</h2>
<div class="abs feature" style="left:185px">
  <div class="feature-icon" role="img" aria-label="Symbol: Person mit Schlüssel"></div>
  <h3>Unabhängig</h3>
  <p>Wir arbeiten nur für dich. Um unabhängig zu bleiben, verzichten wir bewusst auf Provisions-Deals mit Energieanbietern.</p>
</div>
<div class="abs feature" style="left:478px">
  <div class="feature-icon" role="img" aria-label="Symbol: Klemmbrett mit Zahnrad"></div>
  <h3>Automatisch</h3>
  <p>Du meldest dich einmal an und wir übernehmen den Rest. Ganz automatisch.</p>
</div>
<div class="abs feature" style="left:763px">
  <div class="feature-icon" role="img" aria-label="Symbol: Geldschein mit Münze"></div>
  <h3>Fair</h3>
  <p>Voltwise bleibt mehr im Börsel. Trotz Service-Gebühr.</p>
</div>

<h2 class="abs save-title">Wie viel könntest du sparen?</h2>
<div class="abs field" style="left:268px">Enter your Postal code</div>
<div class="abs field" style="left:606px">Enter your Email</div>
<div class="abs btn-teal" style="left:507px;top:2821px;width:188px;height:37px;text-transform:none;font-size:9px">Sehen Sie, wie viel Sie sparen können</div>

<div class="abs logo" style="left:99px;top:2950px">voltwise<span class="dot"></span></div>
<h4 class="abs foot-head" style="left:334px">Company</h4>
<ul class="abs foot-links" style="left:334px"><li>About us</li><li>Contact us</li></ul>
<h4 class="abs foot-head" style="left:513px">Learn &amp; Support</h4>
<ul class="abs foot-links" style="left:513px"><li>How it works</li><li>Energy Guides</li><li>Help</li></ul>
<h4 class="abs foot-head" style="left:693px">Legal</h4>
<ul class="abs foot-links" style="left:693px"><li>Terms and Conditions</li><li>Privacy Policy</li><li>Cookies</li><li>Contact us</li></ul>
<h4 class="abs foot-head" style="left:860px">Follow us</h4>
<div class="abs socials"><span></span><span></span><span></span><span></span><span></span></div>
<p class="abs copyright">© Voltwise. All rights reserved.</p>
</body>
</html>
```